LET ME HANDLE YOUR AUCTION NEEDS!

I am here to handle all your auction needs, I have over 20 years of auction experience buying and selling for dealerships in North Carolina and Tennessee. Send me to the sale to either rep your vehicles or let me know what you need and I can be
another set of eyes to help you buy what is hot and bad credit cars are my specialty. You know a car always sells better with a familiar face rather than auction personnel and with my great reputation I will be able to help find the buyers for your aged inventory.
Call me today and let's get started.
Rick Halvorsen 555-862-3917
(please have pictures of vehicles or an auto auction in the design)

```html
<!DOCTYPE html>
<html lang="en">
<head>
<meta charset="utf-8">
<title>Rick Halvorsen – Auction Services Card</title>
<link rel="stylesheet" href="https://fonts.googleapis.com/css2?family=Roboto+Condensed:wght@300;700&family=Dancing+Script:wght@600&display=swap">
<style>
  :root {
    --page: #ffffff;
    --cream: #ecd2b6;
    --blush: #cdb1a9;
    --pearl: #efe6e2;
    --espresso: #1c1312;
    --cocoa: #3b2218;
    --copper: #9a4e26;
    --name-red: #7a1a17;
    --script-red: #b5322d;
    --white: #ffffff;
    --dot: #a9a9ad;
  }
  * { margin: 0; padding: 0; box-sizing: border-box; }
  html, body {
    width: 1200px; height: 863px; overflow: hidden;
    background: var(--page);
  }
  .canvas { position: relative; width: 1200px; height: 863px; }
  .card {
    position: absolute; left: 0; top: 0;
    width: 594px; height: 863px; overflow: hidden;
    box-shadow: 4px 0 10px rgba(0,0,0,0.35);
  }
  .card-bg { position: absolute; inset: 0; }
  .hero-art {
    position: absolute; left: 158px; top: 42px;
    width: 266px; height: 166px;
    border-radius: 6px;
    background: radial-gradient(ellipse at 35% 70%, #c8502e 0%, #8a5a40 40%, rgba(120,80,60,0.25) 75%, rgba(120,80,60,0) 100%);
  }
  .name {
    position: absolute; left: 0; width: 594px; top: 222px;
    text-align: center;
    font-family: "Roboto Condensed", sans-serif;
    font-weight: 700; font-size: 68px; line-height: 1;
    color: var(--name-red); letter-spacing: -0.5px;
  }
  .phone {
    position: absolute; left: 0; width: 580px; top: 458px;
    text-align: center;
    font-family: "Roboto Condensed", sans-serif;
    font-weight: 700; font-size: 39px; color: var(--white);
  }
  .benefits {
    position: absolute; left: 108px; top: 539px;
    list-style: none;
    font-family: "Roboto Condensed", sans-serif;
    font-weight: 300; font-size: 24px; line-height: 31px;
    color: var(--white);
  }
  .benefits li { display: flex; align-items: center; gap: 10px; }
  .benefits svg { width: 22px; height: 22px; flex: none; }
  .cta {
    position: absolute; left: 0; width: 584px; top: 738px;
    text-align: center;
    font-family: "Dancing Script", cursive;
    font-weight: 600; font-size: 44px;
    color: var(--script-red); transform: rotate(-3deg);
  }
</style>
</head>
<body>
<div class="canvas">
  <div class="card">
    <svg class="card-bg" width="594" height="863" viewBox="0 0 594 863" aria-hidden="true">
      <defs>
        <linearGradient id="top-fill" x1="0" y1="0" x2="1" y2="0">
          <stop offset="0" stop-color="#e8c9a8"/>
          <stop offset="0.3" stop-color="#e6dccb"/>
          <stop offset="0.55" stop-color="#d2b9ad"/>
          <stop offset="0.85" stop-color="#caaea6"/>
          <stop offset="1" stop-color="#ddd0cc"/>
        </linearGradient>
        <radialGradient id="bottom-glow" cx="0.95" cy="0.12" r="0.9">
          <stop offset="0" stop-color="#9e4f24"/>
          <stop offset="0.35" stop-color="#5a2e1c"/>
          <stop offset="0.75" stop-color="#241614"/>
          <stop offset="1" stop-color="#1a1211"/>
        </radialGradient>
        <linearGradient id="band" x1="0" y1="0" x2="1" y2="0">
          <stop offset="0" stop-color="#c79d8f"/>
          <stop offset="0.35" stop-color="#d3b0a6"/>
          <stop offset="0.55" stop-color="#d78a63"/>
          <stop offset="0.75" stop-color="#f4eef0"/>
          <stop offset="1" stop-color="#d9aaa2"/>
        </linearGradient>
      </defs>
      <rect width="594" height="863" fill="url(#bottom-glow)"/>
      <path d="M0 0 H594 V302 C440 318 240 360 0 372 Z" fill="url(#top-fill)"/>
      <path d="M0 372 C240 360 440 318 594 302 V338 C440 350 240 392 0 410 Z" fill="url(#band)"/>
      <path d="M0 372 C240 360 440 318 594 302" fill="none" stroke="#8c6a60" stroke-width="2" opacity="0.6"/>
      <g fill="var(--dot)">
        <circle cx="310" cy="202" r="2.2"/><circle cx="321" cy="202" r="2.2"/><circle cx="332" cy="202" r="2.2"/>
        <circle cx="343" cy="202" r="2.2"/><circle cx="354" cy="202" r="2.2"/><circle cx="365" cy="202" r="2.2"/>
        <circle cx="376" cy="202" r="2.2"/><circle cx="387" cy="202" r="2.2"/><circle cx="398" cy="202" r="2.2"/>
        <circle cx="409" cy="202" r="2.2"/><circle cx="420" cy="202" r="2.2"/><circle cx="431" cy="202" r="2.2"/>
        <circle cx="442" cy="202" r="2.2"/><circle cx="453" cy="202" r="2.2"/><circle cx="464" cy="202" r="2.2"/>
        <circle cx="475" cy="202" r="2.2"/><circle cx="486" cy="202" r="2.2"/>
      </g>
    </svg>

    <div class="hero-art" role="img" aria-label="Auction gavel striking a sound block with an orange sports car on top"></div>

    <h1 class="name">RICK HALVORSEN</h1>
    <p class="phone">555.862.3917</p>

    <ul class="benefits">
      <li><svg viewBox="0 0 22 22"><path d="M3 12 L9 18 L19 3" fill="none" stroke="var(--white)" stroke-width="2.4" stroke-linecap="round" stroke-linejoin="round"/></svg>Over 20 years of auction experience</li>
      <li><svg viewBox="0 0 22 22"><path d="M3 12 L9 18 L19 3" fill="none" stroke="var(--white)" stroke-width="2.4" stroke-linecap="round" stroke-linejoin="round"/></svg>Buying and selling for dealerships</li>
      <li><svg viewBox="0 0 22 22"><path d="M3 12 L9 18 L19 3" fill="none" stroke="var(--white)" stroke-width="2.4" stroke-linecap="round" stroke-linejoin="round"/></svg>Bad credit - No Problem</li>
      <li><svg viewBox="0 0 22 22"><path d="M3 12 L9 18 L19 3" fill="none" stroke="var(--white)" stroke-width="2.4" stroke-linecap="round" stroke-linejoin="round"/></svg>Known reputation</li>
      <li><svg viewBox="0 0 22 22"><path d="M3 12 L9 18 L19 3" fill="none" stroke="var(--white)" stroke-width="2.4" stroke-linecap="round" stroke-linejoin="round"/></svg>I can find your buyers!</li>
    </ul>

    <p class="cta">Call me today!</p>
  </div>
</div>
</body>
</html>
```